Business card design needed

I have a leadership coaching and consultancy business which specialises in the education sector. I would like a clean, professional design). The design needs to speak to strength, support, new learning, connections & a growth mindest.

I am also looking for a unique LOGO. This is very important.

Target Market(s)

Educational Leaders & executives

Industry/Entity Type

Leadership

Contact Information for Business Card

Marisa Holbeck
Principal Coach & Consultant
Marisa Holbeck Coaching & Consulting
0471 362 815
marisa.holbeck@fernmail.example
I also would like my facebook, twitter and linkedin accounts to appear

Logo styles of interest
Lettermark Logo
Requirements
Must have
• A 2 sided business card with contact details on the back
A logo

```html
<!DOCTYPE html>
<html lang="en">
<head>
<meta charset="utf-8">
<title>Marisa Holbeck Coaching &amp; Consulting — Business Card</title>
<link href="https://fonts.googleapis.com/css2?family=Open+Sans:wght@400;700&display=swap" rel="stylesheet">
<style>
  :root {
    --orange: #e8791a;
    --paper: #ffffff;
    --ink: #3a3a3a;
    --rule: #b9b9b9;
    --backdrop: #eeedeb;
  }
  * { box-sizing: border-box; margin: 0; padding: 0; }
  html, body {
    width: 1200px; height: 900px; overflow: hidden;
    background: var(--backdrop);
    font-family: "Open Sans", Arial, sans-serif;
  }
  .canvas {
    width: 1200px; height: 900px;
    display: flex; flex-direction: column;
    align-items: center; justify-content: center; gap: 50px;
  }
  .card {
    position: relative;
    width: 640px; height: 366px;
    box-shadow: 0 2px 10px rgba(0,0,0,0.12);
    overflow: hidden;
  }
  .card--front { background: var(--orange); }
  .card--back { background: var(--paper); }

  .brand-name {
    position: absolute;
    font-weight: 700;
    white-space: nowrap;
    line-height: 1.2;
  }
  .card--front .brand-name {
    left: 70px; top: 160px;
    font-size: 24px; color: var(--paper);
  }
  .card--back .brand-name {
    left: 40px; top: 76px;
    font-size: 22px; color: var(--orange);
  }

  .divider {
    position: absolute; left: 352px; top: 150px;
    width: 1px; height: 110px; background: var(--rule);
  }

  .contacts {
    position: absolute; left: 378px; top: 150px;
    list-style: none;
  }
  .contacts__item {
    display: flex; align-items: center; gap: 9px;
    height: 22px; font-size: 13px; color: var(--orange);
    white-space: nowrap;
  }
  .contacts__icon { width: 12px; height: 12px; flex: none; }

  .person {
    position: absolute; left: 40px; top: 256px;
  }
  .person__name {
    font-size: 21px; font-weight: 700; color: var(--orange);
    letter-spacing: 0.3px; line-height: 1.1;
  }
  .person__title { font-size: 12px; color: var(--ink); }

  .base-stripe {
    position: absolute; left: 0; right: 0; bottom: 26px;
    height: 4px; background: var(--orange);
  }
</style>
</head>
<body>
<main class="canvas">

  <section class="card card--front" aria-label="Card front">
    <p class="brand-name">Marisa Holbeck Coaching &amp; Consulting</p>
  </section>

  <section class="card card--back" aria-label="Card back">
    <p class="brand-name">Marisa Holbeck Coaching &amp; Consulting</p>

    <div class="divider"></div>

    <ul class="contacts">
      <li class="contacts__item">
        <svg class="contacts__icon" viewBox="0 0 12 12" aria-hidden="true">
          <path d="M3 1 L5 3.5 L4 4.8 Q5 7 7.2 8 L8.5 7 L11 9 L9.8 11 Q4.5 10.5 1 3.2 Z" fill="var(--ink)"/>
        </svg>0471 362 815</li>
      <li class="contacts__item">
        <svg class="contacts__icon" viewBox="0 0 12 12" aria-hidden="true">
          <rect x="0.5" y="2.5" width="11" height="7.5" fill="none" stroke="var(--ink)"/>
          <path d="M0.5 2.5 L6 7 L11.5 2.5" fill="none" stroke="var(--ink)"/>
        </svg>marisa.holbeck@fernmail.example</li>
      <li class="contacts__item">
        <svg class="contacts__icon" viewBox="0 0 12 12" aria-hidden="true"><circle cx="6" cy="6" r="5.5" fill="var(--ink)"/></svg>connect.example/holbeck</li>
      <li class="contacts__item">
        <svg class="contacts__icon" viewBox="0 0 12 12" aria-hidden="true"><circle cx="6" cy="6" r="5.5" fill="var(--ink)"/></svg>updates.example/holbeck</li>
      <li class="contacts__item">
        <svg class="contacts__icon" viewBox="0 0 12 12" aria-hidden="true"><circle cx="6" cy="6" r="5.5" fill="var(--ink)"/></svg>network.example/holbeck</li>
    </ul>

    <div class="person">
      <p class="person__name">MARISA HOLBECK</p>
      <p class="person__title">Principal Coach &amp; Consultant</p>
    </div>

    <div class="base-stripe"></div>
  </section>

</main>
</body>
</html>
```